Business Card Design

I am a Special Event Consultant,I arrange and organise Special Events - Product Launches,Sponsorship and Product Displays.

I would like the RTV to be a feature of the design with 'Special Event Services" underneath - keep it very simple but creative using this information. So it is just the letters "RTV" with Event Services underneath.

(Simple Colours - Silver, Black, Grey - no bright colours - We work for Valtoria Drenn,KDX, Lyndrel So it is class and classic.)

Only my Name and mobile on the front.

Contact Information for Business Card

FRONT
Tess Varnholt
Tel: 0436 218907

BACK
Email: tess@rtveventservices.example.au

2807 Wexbury Heights,83 Pollard Street
NORTHVALE.Vic.3158.

```html
<!DOCTYPE html>
<html lang="en">
<head>
<meta charset="utf-8">
<title>Tess Varnholt – RTV Special Event Services</title>
<link rel="stylesheet" href="https://fonts.googleapis.com/css2?family=Roboto+Slab:wght@200;300;400&display=swap">
<style>
  :root {
    --page-bg: #d9d9d9;
    --card-light: #3c3d41;
    --card-dark: #121214;
    --brand-silver: #c8cbd0;
    --name-silver: #b4b8be;
    --service-white: #f1f1f3;
    --label-grey: #8a8d92;
    --accent-grey: #9a9ea4;
    --accent-silver: #c2c5ca;
  }
  html, body {
    margin: 0;
    width: 1200px;
    height: 900px;
    overflow: hidden;
    background: var(--page-bg);
  }
  .canvas {
    position: relative;
    width: 1200px;
    height: 900px;
    display: flex;
    align-items: center;
    justify-content: center;
  }
  .card {
    position: relative;
    width: 910px;
    height: 520px;
    background: radial-gradient(ellipse at 55% 40%, var(--card-light) 0%, var(--card-dark) 88%);
    box-shadow: 0 18px 40px rgba(0, 0, 0, 0.35);
    font-family: "Roboto Slab", Georgia, serif;
  }
  .accent-slash {
    position: absolute;
  }
  .accent-slash--top { left: 560px; top: 92px; }
  .accent-slash--bottom { left: 402px; top: 322px; }
  .identity {
    position: absolute;
    left: 410px;
    top: 150px;
  }
  .identity__brand {
    margin: 0 0 6px;
    color: var(--brand-silver);
    font-weight: 300;
    font-size: 44px;
    letter-spacing: 10px;
    line-height: 1;
  }
  .identity__name {
    margin: 0;
    color: var(--name-silver);
    font-weight: 200;
    font-size: 30px;
    letter-spacing: 1px;
    line-height: 1.15;
  }
  .identity__service {
    margin: 2px 0 0;
    color: var(--service-white);
    font-weight: 300;
    font-size: 24px;
    letter-spacing: 0.5px;
    line-height: 1.15;
  }
  .contact {
    position: absolute;
    left: 0;
    right: 0;
    top: 418px;
    text-align: center;
    font-size: 19px;
    letter-spacing: 1px;
  }
  .contact__label {
    color: var(--label-grey);
    font-weight: 200;
  }
  .contact__number {
    color: var(--service-white);
    font-weight: 300;
  }
  .contact__mark {
    display: block;
    margin: 10px auto 0;
  }
</style>
</head>
<body>
  <main class="canvas">
    <section class="card" aria-label="Business card front">
      <svg class="accent-slash accent-slash--top" width="20" height="60" viewBox="0 0 20 60" aria-hidden="true">
        <line x1="18" y1="2" x2="2" y2="58" stroke="var(--accent-grey)" stroke-width="1.5"/>
      </svg>

      <div class="identity">
        <p class="identity__brand">RTV</p>
        <p class="identity__name">Tess Varnholt</p>
        <p class="identity__service">Special Event Services</p>
      </div>

      <svg class="accent-slash accent-slash--bottom" width="20" height="60" viewBox="0 0 20 60" aria-hidden="true">
        <line x1="18" y1="2" x2="2" y2="58" stroke="var(--accent-grey)" stroke-width="1.5"/>
      </svg>

      <div class="contact">
        <span class="contact__label">Tel:</span>
        <span class="contact__number">0436 218907</span>
        <svg class="contact__mark" width="22" height="8" viewBox="0 0 22 8" aria-hidden="true">
          <polygon points="6,0 22,0 16,8 0,8" fill="var(--accent-silver)"/>
        </svg>
      </div>
    </section>
  </main>
</body>
</html>
```